Garage Door Company seeking business card designs.
Harbor Ridge Door
Professional
Miles Tandry
Owner, Operator.
We don't want a address listed...
Miles@HarborRidgeDoor.com
www.PortalLiftExperts.com
We want to publish three numbers: Pinecrest - 320.555.0147 Maplewood - 320.555.0192 Elm Bay - 952.555.0163 on front... Commercial and Residential On back... New Garage Door Sales and Installation. Repair and Maintenance Services. List website; www.PortalLiftExperts.com Have name, title, phone numbers, email, and website on one side. Motto's and verbiage on the other back side. Logo likely on front very prominently. Front can be full color, and back should be back letter, or the door of the logo lettering.
"If you can't get it up, we can!" Sales and Installation. Repair and Maintenance.

```html
<!DOCTYPE html>
<html lang="en">
<head>
<meta charset="utf-8">
<title>Harbor Ridge Door – Business Cards</title>
<link href="https://fonts.googleapis.com/css2?family=Open+Sans:wght@400;600;700&display=swap" rel="stylesheet">
<style>
  :root {
    --forest: #3f5417;
    --forest-dark: #33460f;
    --paper: #ffffff;
    --ink: #2c3a10;
    --backdrop: #2a2a2a;
    --text-light: #f3f5ec;
  }
  * { box-sizing: border-box; margin: 0; padding: 0; }
  html, body { width: 1200px; height: 904px; overflow: hidden; }
  body {
    background: var(--backdrop);
    font-family: "Open Sans", Arial, sans-serif;
    display: flex;
    flex-direction: column;
    align-items: center;
    justify-content: center;
    gap: 40px;
  }
  .card {
    width: 560px;
    height: 320px;
    border-radius: 16px;
    overflow: hidden;
    position: relative;
  }

  /* Back side: motto and services */
  .card--back {
    background: var(--forest);
    color: var(--text-light);
    text-align: center;
    padding-top: 34px;
  }
  .logo-art {
    display: block;
    margin: 0 auto;
    border-radius: 6px;
  }
  .card--back .logo-art {
    width: 120px;
    height: 62px;
    background: linear-gradient(180deg, #6f7f4d, #4c5e25);
  }
  .brand-name {
    font-family: "Open Sans", Arial, sans-serif;
    font-weight: 700;
    letter-spacing: 0.5px;
    white-space: nowrap;
  }
  .card--back .brand-name {
    font-size: 22px;
    margin-top: 8px;
    color: var(--text-light);
  }
  .motto {
    font-size: 12px;
    margin-top: 14px;
  }
  .services {
    font-size: 12px;
    line-height: 1.45;
    margin-top: 14px;
  }
  .web-rule {
    display: flex;
    align-items: center;
    justify-content: center;
    gap: 10px;
    margin-top: 20px;
    font-size: 12px;
  }
  .web-rule::before, .web-rule::after {
    content: "";
    width: 36px;
    height: 1px;
    background: var(--text-light);
  }

  /* Front side: logo and contacts */
  .card--front { background: var(--paper); }
  .front-shape { position: absolute; inset: 0; }
  .front-logo {
    position: absolute;
    left: 24px;
    top: 118px;
    width: 262px;
    text-align: center;
  }
  .card--front .logo-art {
    width: 150px;
    height: 72px;
    background: linear-gradient(180deg, #5d6f37, #3f5417);
  }
  .card--front .brand-name {
    font-size: 22px;
    margin-top: 8px;
    color: var(--forest);
  }
  .sectors {
    font-size: 13px;
    color: var(--ink);
    margin-top: 4px;
  }
  .contact {
    position: absolute;
    left: 335px;
    top: 72px;
    color: var(--text-light);
    font-size: 11px;
  }
  .contact__name { font-size: 16px; font-weight: 600; }
  .contact__title { font-size: 11px; margin-top: 2px; }
  .contact__list { list-style: none; margin-top: 16px; }
  .contact__list li {
    display: flex;
    align-items: center;
    gap: 8px;
    height: 17px;
    white-space: nowrap;
  }
  .contact__list svg { width: 11px; height: 11px; flex: none; }
</style>
</head>
<body>

  <section class="card card--back" aria-label="Card back">
    <div class="logo-art" role="img" aria-label="Company logo artwork: pine trees behind a garage"></div>
    <div class="brand-name">Harbor Ridge Door</div>
    <p class="motto">"If you can't get it up, we can!"</p>
    <p class="services">Sales and Installation,<br>Repair and Maintenance</p>
    <p class="web-rule">www.PortalLiftExperts.com</p>
  </section>

  <section class="card card--front" aria-label="Card front">
    <svg class="front-shape" viewBox="0 0 560 320" preserveAspectRatio="none" aria-hidden="true">
      <polygon points="270,0 560,0 560,320 300,320 345,200" fill="var(--forest)"/>
    </svg>

    <div class="front-logo">
      <div class="logo-art" role="img" aria-label="Company logo artwork: pine trees behind a garage"></div>
      <div class="brand-name">Harbor Ridge Door</div>
      <p class="sectors">Commercial and Residential</p>
    </div>

    <div class="contact">
      <p class="contact__name">Miles Tandry</p>
      <p class="contact__title">Owner, Operator</p>
      <ul class="contact__list">
        <li><svg viewBox="0 0 12 12"><circle cx="6" cy="6" r="6" fill="#fff"/><path d="M4 3.2l1 1.2-.6.7c.5 1 1.2 1.7 2.2 2.2l.7-.6 1.2 1-.6 1C5.8 8.5 3.6 6.3 3.3 4z" fill="var(--forest)"/></svg>320.555.0147 (Pinecrest)</li>
        <li><svg viewBox="0 0 12 12"><circle cx="6" cy="6" r="6" fill="#fff"/><path d="M4 3.2l1 1.2-.6.7c.5 1 1.2 1.7 2.2 2.2l.7-.6 1.2 1-.6 1C5.8 8.5 3.6 6.3 3.3 4z" fill="var(--forest)"/></svg>320.555.0192 (Maplewood)</li>
        <li><svg viewBox="0 0 12 12"><circle cx="6" cy="6" r="6" fill="#fff"/><path d="M4 3.2l1 1.2-.6.7c.5 1 1.2 1.7 2.2 2.2l.7-.6 1.2 1-.6 1C5.8 8.5 3.6 6.3 3.3 4z" fill="var(--forest)"/></svg>952.555.0163 (Elm Bay)</li>
        <li><svg viewBox="0 0 12 12"><circle cx="6" cy="6" r="6" fill="#fff"/><rect x="3" y="4" width="6" height="4" fill="none" stroke="var(--forest)" stroke-width="0.9"/><path d="M3 4l3 2.2L9 4" fill="none" stroke="var(--forest)" stroke-width="0.9"/></svg>Miles@HarborRidgeDoor.com</li>
        <li><svg viewBox="0 0 12 12"><circle cx="6" cy="6" r="6" fill="#fff"/><circle cx="6" cy="6" r="3.2" fill="none" stroke="var(--forest)" stroke-width="0.9"/><path d="M2.8 6h6.4M6 2.8c-1.4 1.8-1.4 4.6 0 6.4M6 2.8c1.4 1.8 1.4 4.6 0 6.4" fill="none" stroke="var(--forest)" stroke-width="0.7"/></svg>www.PortalLiftExperts.com</li>
      </ul>
    </div>
  </section>

</body>
</html>
```